Portal Panel Medic need professional looking business card printed on plastic, Commericial, Industri

We are family owned and operated garage door company in Indianapolis, Indiana. We sale service and install dock equipment, doors, operators. We are looking to expand our commercial/ industrial division. We also service all residential doors and operators. We are looking for a business that stands out of the crowd. We are committed to have the best customer service in the industry.

Target Market(s)

National and local general contractors, National/ Corpate service accounts,

Industry/Entity Type

Business Service

Contact Information for Business Card

To be printed on plastic stock

Font styles to use
Sans Serif

Colors
ffffff
f04a50
ec1f27

Requirements
Must have
• Name, website,email, phone number, position.
Nice to have
• A standout professional design

```html
<!DOCTYPE html>
<html lang="en">
<head>
<meta charset="utf-8">
<title>Portal Panel Medic – Business Card</title>
<link rel="stylesheet" href="https://fonts.googleapis.com/css2?family=Roboto:wght@400;500;700&family=Open+Sans:wght@600;700&display=swap">
<style>
  :root {
    --page-bg: #e9ebee;
    --card-white: #f3f4f6;
    --brand-red: #ec1f27;
    --deep-red: #c8121a;
    --soft-red: #f04a50;
    --logo-red: #b5141b;
    --ink: #111111;
    --white: #ffffff;
    --pale: #ffe9ea;
  }
  * { margin: 0; padding: 0; box-sizing: border-box; }
  html, body {
    width: 1200px; height: 970px; overflow: hidden;
    background: var(--page-bg);
    font-family: "Roboto", Arial, sans-serif;
  }
  .card {
    position: absolute; left: 80px; top: 188px;
    width: 1040px; height: 593px;
    display: flex;
    box-shadow: 0 18px 40px rgba(0,0,0,.18);
  }
  .card-front {
    position: relative; width: 519px; height: 100%;
    background: linear-gradient(180deg, #f7f8fa 0%, #e6e8ec 100%);
  }
  .divider-rule {
    position: absolute; left: 501px; top: 0; width: 10px; height: 463px;
    background: var(--ink);
  }
  .divider-ticks { position: absolute; left: 501px; top: 470px; }
  .brand-name {
    position: absolute; left: 0; width: 519px; top: 248px;
    display: flex; justify-content: center; align-items: center; gap: 12px;
    font-weight: 700; font-size: 36px; line-height: 44px;
    color: var(--logo-red); letter-spacing: .5px;
  }
  .brand-mark { width: 22px; height: 22px; background: var(--logo-red); }
  .brand-tagline {
    position: absolute; left: 0; width: 519px; top: 364px;
    text-align: center; font-size: 14px; line-height: 18px;
    color: var(--logo-red); font-weight: 500; font-style: italic;
  }
  .brand-phone {
    position: absolute; left: 0; width: 519px; top: 386px;
    text-align: center;
    font-family: "Open Sans", Arial, sans-serif;
    font-weight: 700; color: var(--logo-red); font-size: 40px; line-height: 40px;
  }
  .brand-phone .area { font-size: 28px; font-weight: 600; margin-right: 6px; }
  .card-back {
    position: relative; flex: 1; height: 100%;
    background: linear-gradient(160deg, var(--brand-red) 0%, var(--deep-red) 60%, #b10f16 100%);
    color: var(--white);
  }
  .person { position: absolute; left: 77px; top: 138px; }
  .person-name { font-size: 35px; font-weight: 700; line-height: 1; }
  .person-role { font-size: 26px; font-weight: 400; line-height: 1; margin-top: 2px; }
  .address {
    position: absolute; left: 77px; top: 265px;
    font-size: 24px; line-height: 32px; color: var(--pale);
  }
  .contacts {
    position: absolute; left: 77px; top: 352px; list-style: none;
    font-size: 24px; color: var(--pale);
  }
  .contacts li { display: flex; align-items: center; gap: 12px; height: 35px; }
  .contacts svg { width: 30px; height: 30px; flex: none; }
</style>
</head>
<body>
  <div class="card">
    <section class="card-front">
      <div class="brand-name"><span class="brand-mark"></span>Portal Panel Medic</div>
      <p class="brand-tagline">"Reliable Repairs, Honest Rates"</p>
      <p class="brand-phone"><span class="area">(555)</span>214-0148</p>
      <div class="divider-rule"></div>
      <svg class="divider-ticks" width="10" height="48" viewBox="0 0 10 48">
        <rect y="0" width="10" height="6" fill="#111"/>
        <rect y="10" width="10" height="6" fill="#111"/>
        <rect y="20" width="10" height="6" fill="#111"/>
        <rect y="30" width="10" height="6" fill="#111"/>
        <rect y="40" width="10" height="6" fill="#111"/>
      </svg>
    </section>

    <section class="card-back">
      <div class="person">
        <h1 class="person-name">Daniel Reyes</h1>
        <p class="person-role">Founder</p>
      </div>
      <p class="address">PO BOX 123 your address<br>2nd street Melbourne</p>
      <ul class="contacts">
        <li>
          <svg viewBox="0 0 30 30" aria-hidden="true"><circle cx="15" cy="15" r="13" fill="none" stroke="#ffe9ea" stroke-width="2"/><path d="M9 13c0-3 3-4 6-4s6 1 6 4h-3v-1h-6v1zM10 15h10l1 5H9z" fill="#ffe9ea"/></svg>
          <span>(123) 456-7890</span>
        </li>
        <li>
          <svg viewBox="0 0 30 30" aria-hidden="true"><circle cx="15" cy="15" r="13" fill="none" stroke="#ffe9ea" stroke-width="2"/><rect x="8.5" y="10" width="13" height="10" fill="none" stroke="#ffe9ea" stroke-width="1.8"/><path d="M8.5 10l6.5 5.5L21.5 10M8.5 20l5-4.5M21.5 20l-5-4.5" fill="none" stroke="#ffe9ea" stroke-width="1.5"/></svg>
          <span>Info@companygmail.com</span>
        </li>
        <li>
          <svg viewBox="0 0 30 30" aria-hidden="true"><circle cx="15" cy="15" r="13" fill="none" stroke="#ffe9ea" stroke-width="2"/><circle cx="15" cy="15" r="7.5" fill="none" stroke="#ffe9ea" stroke-width="1.5"/><ellipse cx="15" cy="15" rx="3.2" ry="7.5" fill="none" stroke="#ffe9ea" stroke-width="1.3"/><path d="M7.5 15h15M9 11h12M9 19h12" stroke="#ffe9ea" stroke-width="1.2"/></svg>
          <span>www.yourcompany.com</span>
        </li>
      </ul>
    </section>
  </div>
</body>
</html>
```